Signage for a store*

logo on the two sides of the sign
in the middle is the name of the store witch is VORELT
at the bottom of the two logos, one side for location/address and the other side is contact details phone number is 718-392-6107 address is 2974 THE SIGN WILL BEE 15 FEET BY 4 FEET I WOULD LIKE THAT THE
BACKGROUND OF THE SIGN SHOULD HAVE A NICE COLOR BASE
THAT GOES FOR A WINE STORE

```html
<!DOCTYPE html>
<html lang="en">
<head>
<meta charset="utf-8">
<title>VORELT – Store Signage</title>
<link href="https://fonts.googleapis.com/css2?family=Poppins:ital,wght@0,400;1,600;1,700&display=swap" rel="stylesheet">
<style>
  :root {
    --wine: #a3305a;
    --wine-deep: #952a52;
    --wine-soft: #d994ad;
    --gold: #97762a;
    --paper: #ffffff;
    --frame: #c8c8c8;
    --text-light: #ffffff;
  }
  * { box-sizing: border-box; margin: 0; padding: 0; }
  html, body { width: 1200px; height: 1200px; overflow: hidden; background: var(--paper); }
  .canvas {
    position: relative; width: 1200px; height: 1200px;
    border: 1px solid var(--frame); background: var(--paper);
    font-family: "Poppins", sans-serif;
  }
  .sign {
    position: absolute; left: 30px; width: 1140px; height: 303px;
    background: var(--paper); border: 1px solid #e6e6e6; overflow: hidden;
  }
  .sign--phone { top: 280px; }
  .sign--address { top: 616px; }
  .sign__edge { position: absolute; left: 0; top: 0; width: 27px; height: 100%; background: var(--gold); }
  .sign__wash {
    position: absolute; left: 300px; top: 0; width: 840px; height: 100%;
    background:
      radial-gradient(ellipse 60% 80% at 85% 50%, var(--wine-deep) 0%, transparent 70%),
      linear-gradient(90deg, rgba(255,255,255,0) 0%, rgba(217,148,173,0.75) 22%, var(--wine) 52%, var(--wine) 100%);
  }
  .brand { position: absolute; left: 102px; top: 24px; width: 192px; height: 256px; }
  .brand__ornament { position: absolute; left: 18px; width: 156px; border-radius: 50%; }
  .brand__ornament--top {
    top: 0; height: 96px;
    background: radial-gradient(circle at 50% 55%, rgba(151,118,42,0.35), rgba(149,42,82,0.22) 60%, rgba(149,42,82,0.05));
  }
  .brand__ornament--bottom {
    top: 160px; height: 96px; left: 30px; width: 132px;
    background: radial-gradient(circle at 50% 45%, rgba(149,42,82,0.25), rgba(151,118,42,0.1) 70%, rgba(255,255,255,0));
  }
  .brand__name {
    position: absolute; left: 0; top: 104px; width: 192px; text-align: center;
    font-family: "Poppins", sans-serif; font-weight: 400; font-size: 40px;
    letter-spacing: 1px; color: var(--wine-deep); line-height: 48px;
  }
  .message { position: absolute; left: 560px; width: 560px; text-align: center; color: var(--text-light); font-style: italic; font-weight: 700; }
  .message__lead { font-weight: 600; font-size: 33px; line-height: 40px; }
  .message__rule { position: relative; height: 14px; margin: 0 auto; }
  .message__rule svg { display: block; margin: 0 auto; }
  .message__big { font-size: 58px; line-height: 66px; letter-spacing: 0.5px; }
  .message--phone { top: 88px; }
  .message--address { top: 58px; }
</style>
</head>
<body>
<main class="canvas">

  <section class="sign sign--phone">
    <div class="sign__edge"></div>
    <div class="sign__wash" role="img" aria-label="Wine-coloured watercolour wash with splashes"></div>
    <div class="brand">
      <div class="brand__ornament brand__ornament--top" role="img" aria-label="Decorative grape and vine ornament"></div>
      <div class="brand__name">VORELT</div>
      <div class="brand__ornament brand__ornament--bottom" role="img" aria-label="Decorative leaf ornament"></div>
    </div>
    <div class="message message--phone">
      <p class="message__lead">oder now!</p>
      <div class="message__rule">
        <svg width="310" height="14" viewBox="0 0 310 14">
          <line x1="4" y1="7" x2="134" y2="7" stroke="#fff" stroke-width="1.5"/>
          <circle cx="157" cy="7" r="5.5" fill="#fff"/>
          <line x1="182" y1="7" x2="310" y2="7" stroke="#fff" stroke-width="1.5"/>
        </svg>
      </div>
      <p class="message__big">718-392-6107</p>
    </div>
  </section>

  <section class="sign sign--address">
    <div class="sign__edge"></div>
    <div class="sign__wash" role="img" aria-label="Wine-coloured watercolour wash with splashes"></div>
    <div class="brand">
      <div class="brand__ornament brand__ornament--top" role="img" aria-label="Decorative grape and vine ornament"></div>
      <div class="brand__name">VORELT</div>
      <div class="brand__ornament brand__ornament--bottom" role="img" aria-label="Decorative leaf ornament"></div>
    </div>
    <div class="message message--address">
      <p class="message__lead">come and taste!</p>
      <div class="message__rule">
        <svg width="310" height="14" viewBox="0 0 310 14">
          <line x1="0" y1="7" x2="128" y2="7" stroke="#fff" stroke-width="1.5"/>
          <circle cx="152" cy="7" r="5.5" fill="#fff"/>
          <line x1="176" y1="7" x2="306" y2="7" stroke="#fff" stroke-width="1.5"/>
        </svg>
      </div>
      <p class="message__big">2974 Harlow St</p>
      <p class="message__big">Brenton, N.Y. 11093</p>
    </div>
  </section>

</main>
</body>
</html>
```